Maison Vurel

menu design, menu change,
will send hand written rough draft soon
Updates

Project Deadline Extended
Reason: Got off to a slow start. Things are progressing now. Thank you.

Target Market(s)

18-60 yr olds, blue collar & professionals, middle class, median income, families,upscale - casual- steakhouse concept

Industry/Entity Type

Restaurant

Colors
f68d4c
f37122
f78f20
faa54b
ffc214
fece3e
fbee3e
fbed22
333333

Requirements
Must have
• Front cover, back cover. 2 inside views
Nice to have
• 8 x 14 page size

```html
<!DOCTYPE html>
<html lang="en">
<head>
<meta charset="utf-8">
<title>Maison Vurel – Menu</title>
<link href="https://fonts.googleapis.com/css2?family=Raleway:wght@300;400;500&family=Open+Sans:wght@400;600&display=swap" rel="stylesheet">
<style>
  :root {
    --page: #ffffff;
    --board: #333333;
    --gold: #c9aa6c;
    --gold-band: #c7a568;
    --name: #e6d3a8;
    --desc: #e4e0d8;
    --ink-dark: #2a2622;
  }
  * { margin: 0; padding: 0; box-sizing: border-box; }
  html, body { width: 1200px; height: 1000px; overflow: hidden; background: var(--page); }
  .canvas { position: relative; width: 1200px; height: 1000px; }

  .board { position: absolute; top: 177px; height: 645px; background: var(--board); }
  .board--left { left: 34px; width: 566px; }
  .board--right { left: 600px; width: 566px; }
  .spine { position: absolute; left: 599px; top: 177px; width: 2px; height: 645px; background: var(--gold); }

  .heading {
    position: absolute; font-family: "Raleway", sans-serif; font-weight: 400;
    font-size: 20px; letter-spacing: .6px; color: var(--gold); text-align: center;
    transform: translateX(-50%); white-space: nowrap; line-height: 1;
  }
  .subhead {
    position: absolute; font-family: "Open Sans", sans-serif; font-weight: 400; font-size: 8px;
    color: var(--desc); text-align: center; transform: translateX(-50%);
    white-space: nowrap; letter-spacing: .2px; line-height: 1;
  }

  .item { position: absolute; }
  .item.ruled { border-bottom: 1px solid var(--gold); padding-bottom: 2px; }
  .row { display: flex; justify-content: space-between; align-items: baseline; }
  .name { font-family: "Raleway", sans-serif; font-size: 14.5px; color: var(--name); line-height: 16px; white-space: nowrap; }
  .price { font-family: "Open Sans", sans-serif; font-size: 8.5px; color: var(--desc); white-space: nowrap; }
  .desc { font-family: "Open Sans", sans-serif; font-size: 7px; color: var(--desc); line-height: 10.5px; white-space: nowrap; }

  .dashed { position: absolute; left: 42px; top: 270px; width: 544px; border-top: 2px dashed var(--desc); }

  .brand { position: absolute; text-align: center; font-family: "Raleway", sans-serif; color: var(--gold); line-height: 1; }
  .brand__name { font-size: 15px; font-weight: 400; }
  .brand__tag { font-size: 7px; font-weight: 400; margin-top: 3px; }

  .list { position: absolute; font-family: "Open Sans", sans-serif; font-size: 9.5px; color: var(--name); }
  .list li { list-style: none; display: flex; justify-content: space-between; line-height: 12px; }
  .list .note { font-size: 7px; color: var(--desc); line-height: 10px; }

  .choices { position: absolute; left: 334px; top: 764px; width: 250px; font-family: "Raleway", sans-serif; font-size: 10.5px; color: var(--name); letter-spacing: .8px; line-height: 12px; white-space: nowrap; }

  .advisory {
    position: absolute; left: 34px; top: 803px; width: 566px; height: 19px; background: var(--gold-band);
    font-family: "Open Sans", sans-serif; font-weight: 600; font-size: 6.8px; color: var(--ink-dark);
    padding-left: 11px; line-height: 19px; white-space: nowrap;
  }
</style>
</head>
<body>
<div class="canvas">
  <div class="board board--left"></div>
  <div class="board board--right"></div>
  <div class="spine"></div>

  <!-- Left page -->
  <h2 class="heading" style="left:317px;top:188px">THIS IS CATTLE COUNTRY!</h2>
  <p class="subhead" style="left:317px;top:212px">ALL SERVED WITH CHOICE OF POTATO &amp; HOT BREAD</p>
  <div class="brand" style="left:482px;top:192px;width:100px">
    <div class="brand__name">Maison Vurel</div>
    <div class="brand__tag">Steaks &amp; Spirits</div>
  </div>

  <div class="item" style="left:55px;top:236px;width:245px">
    <div class="row"><span class="name">Chicken Fried Steak</span><span class="price">12.99</span></div>
    <p class="desc">Hand breaded | Country Gravy</p>
  </div>
  <div class="item" style="left:334px;top:236px;width:246px">
    <div class="row"><span class="name">Mushroom Ground Sirloin Steak</span><span class="price">12.99</span></div>
    <p class="desc">14 oz ground sirloins | Beef mushroom gravy</p>
  </div>
  <div class="dashed"></div>

  <div class="item ruled" style="left:55px;top:281px;width:245px">
    <div class="row"><span class="name">Parmesian Pepper Press Steak*</span><span class="price">19.99</span></div>
    <p class="desc">12 oz choice tenderloin cut | Parmesian Pepper Crust</p>
  </div>
  <div class="item" style="left:55px;top:323px;width:245px">
    <div class="row"><span class="name">Steak Chateau Briand*</span><span class="price">19.99</span></div>
    <p class="desc">12 oz choice tenderloin cut | Parmesian cream sauce |<br>Grilled asparagus spears</p>
  </div>
  <div class="item ruled" style="left:334px;top:281px;width:246px">
    <div class="row"><span class="name">Steak Del Rio*</span><span class="price">19.99</span></div>
    <p class="desc">12 oz choice tenderloin cut | Bold Southwestern spices |<br>Chili pepper butter | Fried onion tanglers</p>
  </div>
  <div class="item" style="left:334px;top:325px;width:246px">
    <div class="row"><span class="name">Boston Bleu Cheese Steak*</span><span class="price">19.99</span></div>
    <p class="desc">12 oz choice tenderloin cut | Melting bleu cheese crumbles</p>
  </div>

  <h2 class="heading" style="left:317px;top:380px">VUREL PREMIUM STEAK SELECTIONS</h2>
  <p class="subhead" style="left:317px;top:402px">- CHOICE AND PRIME GRADE BEEF - SERVED WITH HOUSE SALAD, CHOICE OF POTATO &amp; HOT BREAD</p>

  <div class="item ruled" style="left:55px;top:424px;width:245px">
    <div class="row"><span class="name">Filet Mignon*</span><span class="price">(8oz) 24.99 &nbsp;&nbsp; (10oz) 28.99</span></div>
    <p class="desc">Bacon wrapped | The most tender cut</p>
  </div>
  <div class="item" style="left:55px;top:457px;width:245px">
    <div class="row"><span class="name">Kansas City Strip*</span><span class="price">(16oz) 26.99</span></div>
    <p class="desc">Firmer texture | Full of flavor</p>
  </div>
  <div class="item ruled" style="left:334px;top:424px;width:246px">
    <div class="row"><span class="name">Ribeye Steak*</span><span class="price">(16oz) 28.99</span></div>
    <p class="desc">Well marbeled | Rich | Full of flavor | Cut from the prime rib</p>
  </div>
  <div class="item" style="left:334px;top:457px;width:246px">
    <div class="row"><span class="name">Beef Tenderloin Ka-Bob*</span><span class="price">(8 oz) 28.99</span></div>
    <p class="desc">8 oz beef tenderloin | Bell peppers | Onions | Tomatoes |<br>Mushrooms | Pineapple | Light Italian marinade</p>
  </div>

  <h2 class="heading" style="left:317px;top:509px">CHICKEN &amp; SEAFOOD</h2>
  <p class="subhead" style="left:317px;top:531px">SERVED WITH CHOICE OF POTATO &amp; HOT BREAD</p>

  <div class="item ruled" style="left:55px;top:551px;width:245px">
    <div class="row"><span class="name">Charbroiled Chicken Breast</span><span class="price">14.99</span></div>
    <p class="desc">10 oz flame broiled breast</p>
  </div>
  <div class="item ruled" style="left:55px;top:581px;width:245px">
    <div class="row"><span class="name">Fried Chicken Breast</span><span class="price">14.99</span></div>
    <p class="desc">10 oz breast | Corn on the cob | Mashed potatoes | Country gravy</p>
  </div>
  <div class="item ruled" style="left:55px;top:610px;width:245px">
    <div class="row"><span class="name">Hand Breaded Chicken Strips</span><span class="price">9.99</span></div>
    <p class="desc">Cut &amp; breaded per order</p>
  </div>
  <div class="item" style="left:55px;top:640px;width:245px">
    <div class="row"><span class="name">Chicken Ka-Bob</span><span class="price">19.99</span></div>
    <p class="desc">10 oz charbroiled breast | Skewered with bell peppers | Onion |<br>Mushrooms | Tomatoes | Pineapple | light Italian marinade</p>
  </div>

  <div class="item ruled" style="left:334px;top:551px;width:246px">
    <div class="row"><span class="name">North Atlantic Salmon</span><span class="price">17.99</span></div>
    <p class="desc">Charbroiled fillet 8 oz</p>
  </div>
  <div class="item ruled" style="left:334px;top:581px;width:246px">
    <div class="row"><span class="name">English Style Cod</span><span class="price">19.99</span></div>
    <p class="desc">House battered Icelandic Cod loins</p>
  </div>
  <div class="item ruled" style="left:334px;top:610px;width:246px">
    <div class="row"><span class="name">Deep Fried Gulf Shrimp</span><span class="price">17.99</span></div>
    <p class="desc">6 jumbo shrimp</p>
  </div>
  <div class="item ruled" style="left:334px;top:640px;width:246px">
    <div class="row"><span class="name">Mahi Mahi</span><span class="price">19.99</span></div>
    <p class="desc">9 oz charbroiled | Shrimp | Mushroom | White sauce | Vegetables</p>
  </div>
  <div class="item" style="left:334px;top:675px;width:246px">
    <div class="row"><span class="name">Country Fried Catfish</span><span class="price">12.99</span></div>
    <p class="desc">Catfish fillets | Hand broiled | Deep fried</p>
  </div>

  <h2 class="heading" style="left:180px;top:693px">SIDES</h2>
  <ul class="list" style="left:56px;top:718px;width:242px">
    <li><span>Steamed Garden Vegetables</span><span>4.99</span></li>
    <li><span>Twice Baked Potato</span><span>4.99</span></li>
    <li><span>Loaded Baked &amp; Mashed Potato</span><span>4.99</span></li>
    <li><span>Grilled Asparagus</span><span>4.99</span></li>
    <li><span>House Of Caesar Salad</span><span>4.99</span></li>
    <li class="note"><span>*If in place of potato, add 2.99</span></li>
  </ul>

  <h2 class="heading" style="left:456px;top:737px">POTATO CHOICE</h2>
  <p class="choices">Baked &nbsp;| &nbsp;Mashed &nbsp;| &nbsp;American Fries &nbsp;|<br>German Fries &nbsp;| &nbsp;French Fries &nbsp;| &nbsp;Onion Rings</p>

  <div class="advisory">CONSUMER ADVISORY: CONSUMING RAW OR UNDER COOKED MEAT, POULTRY, SEAFOOD, SHELLFISH, OR EGGS MAY INCREASE YOUR RISK OF FOODBORNE ILLNESS</div>

  <!-- Right page -->
  <h2 class="heading" style="left:883px;top:188px">APPETIZERS</h2>

  <div class="item ruled" style="left:615px;top:208px;width:269px">
    <div class="row"><span class="name">Fried Mozzarella Cheese Sticks</span><span class="price">8.99</span></div>
    <p class="desc">Hand breaded sticks | Marinate sauce</p>
  </div>
  <div class="item ruled" style="left:615px;top:243px;width:269px">
    <div class="row"><span class="name">French Fried Pickles</span><span class="price">8.99</span></div>
  </div>
  <div class="item ruled" style="left:615px;top:272px;width:269px">
    <div class="row"><span class="name">Onion Ring Tower</span><span class="price">8.99</span></div>
  </div>
  <div class="item ruled" style="left:615px;top:296px;width:269px">
    <div class="row"><span class="name">Cheddar Cheese Jalapeno Peppers</span><span class="price">9.99</span></div>
  </div>
  <div class="item" style="left:615px;top:320px;width:269px">
    <div class="row"><span class="name">Calamari</span><span class="price">12.99</span></div>
    <p class="desc">Hand breaded | Cocktail sauce</p>
  </div>

  <div class="item ruled" style="left:908px;top:208px;width:244px">
    <div class="row"><span class="name">Shrimp Cocktail</span><span class="price">11.99</span></div>
    <p class="desc">10 chilled shrimp | Cocktail sauce</p>
  </div>
  <div class="item ruled" style="left:908px;top:242px;width:244px">
    <div class="row"><span class="name">Macha Nachos</span><span class="price">9.99</span></div>
    <p class="desc">Corn tortilla chips | Refried beans | Taromaat | Chili | Cheese |<br>Salsa | Lettuce | Tomato | Jalapenos | Sour cream</p>
  </div>
  <div class="item" style="left:908px;top:295px;width:244px">
    <div class="row"><span class="name">Rocky Mountain Oysters</span><span class="price">12.99</span></div>
    <p class="desc">Full pound of breaded &amp; fried oysters | Homemade sauce</p>
  </div>

  <h2 class="heading" style="left:883px;top:345px">SALADS</h2>

  <div class="item ruled" style="left:615px;top:366px;width:269px">
    <div class="row"><span class="name">Classic Chef Salad</span><span class="price">9.99</span></div>
    <p class="desc">Tossed iceberg lettuce | Cheese | Tomato | Cucumber | Egg |<br>Ham | Turkey | Bacon | Croutons | Garlic breadstick</p>
  </div>
  <div class="item ruled" style="left:615px;top:409px;width:269px">
    <div class="row"><span class="name">Blackened Chicken Southwest Salad</span><span class="price">9.99</span></div>
    <p class="desc">Blackened chicken | Iceburg lettuce | Cheese | Tomato | Sweet corn |<br>Black beans | Black olives | Avocados | Sour cream | Tortilla chips |<br>Southwest dressing</p>
  </div>
  <div class="item" style="left:615px;top:461px;width:269px">
    <div class="row"><span class="name">Caprese Salad</span><span class="price">9.99</span></div>
    <p class="desc">Fresh baby spinach | Fresh mozzarella | Tomato | Balsamic vinegar |<br>Basil</p>
  </div>

  <div class="item ruled" style="left:908px;top:366px;width:244px">
    <div class="row"><span class="name">West Coast Berry Salad</span><span class="price">9.99</span></div>
    <p class="desc">Romaine lettuce | Black cheese | Egg | Tomato | Black &amp; blue<br>berries | Strawberry | Pineapple | Oranges | Almonds | Candried<br>walnuts | Cranberries | Croutons | Raspberry vinegreitte |<br>Chicken or shrimp</p>
  </div>
  <div class="item" style="left:908px;top:433px;width:244px">
    <div class="row"><span class="name">Chicken Salad</span><span class="price">9.99</span></div>
    <p class="desc">Fried or charbroiled chicken | Iceburg lettuce | Cheese | Egg |<br>Tomato | Cucumber | Bacon | Croutons | Garlic breadstick</p>
  </div>

  <h2 class="heading" style="left:883px;top:496px">GOURMET BURGERS</h2>
  <p class="subhead" style="left:883px;top:517px">ALL SERVED WITH BOTTLENECK FRIES</p>

  <div class="item ruled" style="left:615px;top:534px;width:269px">
    <div class="row"><span class="name">Vurel Burger</span><span class="price">9.99</span></div>
    <p class="desc">Cheddar cheese | Smoked ham | Bacon</p>
  </div>
  <div class="item ruled" style="left:615px;top:567px;width:269px">
    <div class="row"><span class="name">Swiss Mushroom</span><span class="price">9.99</span></div>
    <p class="desc">Swiss cheese | Bacon | Sauteed mushrooms</p>
  </div>
  <div class="item" style="left:615px;top:600px;width:269px">
    <div class="row"><span class="name">Bacon Cheddar</span><span class="price">9.99</span></div>
    <p class="desc">Cheddar cheese | Bacon | Brioche bun</p>
  </div>
  <div class="item ruled" style="left:908px;top:534px;width:244px">
    <div class="row"><span class="name">Great Western</span><span class="price">9.99</span></div>
    <p class="desc">Cheddar cheese | Bacon | Onion rings | Harlan's BBQ sauce</p>
  </div>
  <div class="item ruled" style="left:908px;top:567px;width:244px">
    <div class="row"><span class="name">Ranch House Burger</span><span class="price">9.99</span></div>
    <p class="desc">Cheddar cheese | Bacon | Fried egg</p>
  </div>
  <div class="item" style="left:908px;top:600px;width:244px">
    <div class="row"><span class="name">Fire House Burger</span><span class="price">9.99</span></div>
    <p class="desc">Pepper jack cheese | Bacon | Grilled onions | Jalapenos |<br>Hot buffalo sauce</p>
  </div>

  <h2 class="heading" style="left:883px;top:649px">SIGNATURE SANDWICHES</h2>

  <div class="item ruled" style="left:615px;top:676px;width:269px">
    <div class="row"><span class="name">Turkey Avocado Cream Cheese</span><span class="price">9.99</span></div>
    <p class="desc">Smoked turkey | Lettuce | Tomato | Cucumber | Avocados |<br>Cream cheese | Honey mustard | Warm Ciabotta bun</p>
  </div>
  <div class="item ruled" style="left:615px;top:719px;width:269px">
    <div class="row"><span class="name">French Dip</span><span class="price">9.99</span></div>
    <p class="desc">Beef | Provotone cheese | Red onion slices | 12" Hogie | Aujus</p>
  </div>
  <div class="item" style="left:615px;top:752px;width:269px">
    <div class="row"><span class="name">Classic Clubhouse Sandwich</span><span class="price">9.99</span></div>
    <p class="desc">Ham | Turkey | Lettuce | Tomato | Pickle | Onion | Bacon |<br>Cheddar &amp; Swiss cheese | 2 sauces | 3 toasted country style<br>bread slices</p>
  </div>

  <div class="item ruled" style="left:908px;top:676px;width:244px">
    <div class="row"><span class="name">3 Layer Reuben</span><span class="price">9.99</span></div>
    <p class="desc">Corned beef | Kraut | Swiss &amp; cheddar cheese | 1000 island<br>sauce | 3 grilled slices of marble Rye bread</p>
  </div>
  <div class="item ruled" style="left:908px;top:719px;width:244px">
    <div class="row"><span class="name">Chicken Club Sandwich</span><span class="price">9.99</span></div>
    <p class="desc">Hand breaded chicken breast | Provolone cheese | Bacon |<br>Lettuce | Tomato | Pickle | Brioche bun</p>
  </div>
  <div class="item" style="left:908px;top:762px;width:244px">
    <div class="row"><span class="name">Chicken Quesadilla</span><span class="price">9.99</span></div>
    <p class="desc">Fajita seasoned chicken | Jack &amp;<br>cheddar cheese | Grilled in a 12"<br>flour tortilla | Salsa | Sour cream</p>
  </div>
  <div class="brand" style="left:1052px;top:785px;width:100px">
    <div class="brand__name">Maison Vurel</div>
    <div class="brand__tag">Steaks &amp; Spirits</div>
  </div>
</div>
</body>
</html>
```